Magazine Ad for the Waste Industry

We need a full page ad design that will help us introduce our new engine cooling system into the Waste market. This system helps regulate engine temperatures for large trash trucks with its advanced technology and durable. We would like this ad to make an impact and stand out from the more cluttered looking ads that are seen in trade magazines.
The project must be submitted in either InDesign or Photoshop files.

Target Market(s)

Waste Industry, Trash truck manufacturers

Industry/Entity Type

Waste Management

Font styles to use
Sans Serif

Colors
0255a3

Requirements
Must have
• The text and images attached with a more modern industrial/masculine feel.
• Our Company colors are...
• Blue (RGB 25, 76, 159)
• Gray (RGB 129, 130, 133)
• White and black as accents as needed
• SIZING
• Spread Bleed: 9.5" x 11.375"
Nice to have
• I attached two files for a font that we have used in the past. Another font we use commonly is Ariel.

```html
<!DOCTYPE html>
<html lang="en">
<head>
<meta charset="utf-8">
<title>Advanced Electric Engine Cooling – Full Page Ad</title>
<link href="https://fonts.googleapis.com/css2?family=Oswald:wght@400;600;700&family=Roboto:wght@400;500;700&display=swap" rel="stylesheet">
<style>
  :root {
    --brand-blue: #0255a3;
    --deep-indigo: #1a0f5c;
    --violet: #5b2bc4;
    --ink: #07051f;
    --white: #ffffff;
    --soft-white: #d9dcf2;
    --gray: #818285;
  }
  * { margin: 0; padding: 0; box-sizing: border-box; }
  html, body {
    width: 798px; height: 1200px; overflow: hidden;
    background: var(--ink);
  }
  .ad {
    position: relative;
    width: 798px; height: 1200px;
    overflow: hidden;
    background:
      radial-gradient(ellipse 70% 45% at 62% 32%, rgba(110, 60, 230, 0.75), transparent 70%),
      linear-gradient(180deg, var(--deep-indigo) 0%, #3a1fa0 30%, var(--violet) 52%, #241070 78%, var(--ink) 100%);
    font-family: "Roboto", Arial, sans-serif;
    color: var(--white);
  }
  .headline {
    position: absolute; left: 0; right: 0; top: 150px;
    text-align: center;
    font-family: "Oswald", Arial, sans-serif;
    text-transform: uppercase;
    line-height: 1;
  }
  .headline .kicker {
    display: block;
    font-size: 34px; font-weight: 600; letter-spacing: 1px;
    color: var(--soft-white);
  }
  .headline .main {
    display: block; margin-top: 8px;
    font-size: 74px; font-weight: 700; letter-spacing: 1px;
  }
  .product-visual {
    position: absolute; left: 440px; top: 290px;
    width: 320px; height: 330px;
    border-radius: 6px;
    background: radial-gradient(circle at 50% 45%, #3a3d4a 0%, #1a1b24 65%, #0c0c14 100%);
    box-shadow: 0 20px 40px rgba(0,0,0,0.45);
  }
  .benefits {
    position: absolute; left: 60px; top: 330px;
    list-style: none;
    font-size: 22px; font-weight: 700;
    line-height: 1.6;
  }
  .benefits li { display: flex; align-items: center; gap: 12px; }
  .benefits li::before {
    content: ""; width: 10px; height: 10px; border-radius: 50%;
    background: var(--white); flex: none;
  }
  .contact {
    position: absolute; left: 60px; top: 930px;
  }
  .contact .prompt { font-size: 16px; font-weight: 500; color: var(--soft-white); }
  .contact .url { font-size: 24px; font-weight: 700; margin-top: 4px; }
  .contact .lines {
    display: flex; gap: 22px; margin-top: 16px;
    font-size: 14px; color: var(--soft-white);
  }
  .contact .lines span { display: flex; align-items: center; gap: 6px; }
  .contact svg { width: 16px; height: 16px; fill: var(--white); }
  .brand-block {
    position: absolute; right: 50px; top: 935px;
    display: flex; align-items: center; gap: 18px;
  }
  .brand-name {
    font-family: "Oswald", Arial, sans-serif;
    font-weight: 700; font-size: 40px;
    color: var(--white); text-transform: uppercase;
  }
  .badge {
    width: 58px; height: 58px; border-radius: 50%;
    background: var(--gray);
  }
  .badge.large { width: 72px; height: 72px; background: var(--brand-blue); }
</style>
</head>
<body>
  <main class="ad">
    <h1 class="headline">
      <span class="kicker">Advanced Electric</span>
      <span class="main">Engine Cooling</span>
    </h1>

    <div class="product-visual" role="img" aria-label="Product photo of the four-fan electric engine cooling module"></div>

    <ul class="benefits">
      <li>Fully Reversible Fans</li>
      <li>Eliminate Preventative Maintenance</li>
      <li>Average 8% Fuel Economy</li>
      <li>Increase Horsepower</li>
      <li>Quieter Residential Operation</li>
    </ul>

    <section class="contact">
      <p class="prompt">Need to know more? Visit</p>
      <p class="url">www.veltrex-cooling.com/refuse</p>
      <div class="lines">
        <span>
          <svg viewBox="0 0 16 16"><path d="M1 3h14v10H1z M1 3l7 5 7-5" fill="none" stroke="#fff" stroke-width="1.4"/></svg>
          products@veltrex-cooling.com
        </span>
        <span>
          <svg viewBox="0 0 16 16"><circle cx="8" cy="8" r="6.3" fill="none" stroke="#fff" stroke-width="1.4"/><path d="M1.7 8h12.6M8 1.7c3 3.5 3 9 0 12.6M8 1.7c-3 3.5-3 9 0 12.6" fill="none" stroke="#fff" stroke-width="1.1"/></svg>
          veltrex-cooling.com
        </span>
        <span>
          <svg viewBox="0 0 16 16"><path d="M4 1.5l2.2 3-1.4 1.6c.9 2 2.4 3.5 4.4 4.4l1.6-1.4 3 2.2-1.4 2.7C7.5 14 2 8.5 1.3 3z"/></svg>
          (555) 014-2290
        </span>
      </div>
    </section>

    <div class="brand-block">
      <span class="brand-name">Veltrex</span>
      <span class="badge"></span>
      <span class="badge large"></span>
    </div>
  </main>
</body>
</html>
```